Modern Consulting PowerPoint Template

Corvenna Partners needs a PowerPoint template to use for sales proposals, internal meetings, overview decks, etc. Corvenna Partners has acquired 6 companies, and is in the process of consolidating brands. The brand is evolving and wants to adapt to current trends. Corvenna Partners is an accounting and finance consulting firm with expertise in technology and automation. The company currently uses unorganized, dated templates, with lots of white space and no consistency in graphics/tables. The marketing team has attempted to create an improved deck, but the theme is still dated (example attached). The team does not want skyscrapers/buildings. The team wants a theme that has more geometric/fluid shapes, numbers, consistency, and more muted blues/greys/oranges. We request 8 slides that can house information across different decks and are editable:
1. Title Slide
2. Full text/content Slide
3. Half text/content split screen slide with the right side having a modern visual/theme
4. Slide with consistent tables/graphs/graphics/SmartArt ideas
5. Slide for images/logosplashes, potentially with a border to highlight the inserted images
6. Divider slide introducing a new section
7. Contact information/biography slide
8. Closing slide
Industry/Entity Type
Accounting, Finance, and Technology Consulting
Font styles to use
Requirements
Should not have
- Skyscrapers/buildings

```html
<!DOCTYPE html>
<html lang="en">
<head>
<meta charset="utf-8">
<title>Corvenna Partners – Presentation Template Overview</title>
<link href="https://fonts.googleapis.com/css2?family=Montserrat:wght@400;500;600;700;800&family=Open+Sans:wght@400;600&display=swap" rel="stylesheet">
<style>
:root{
  --blue:#2c64a8;
  --blue-dark:#1f4f8c;
  --orange:#f07a22;
  --ink:#333a44;
  --grey:#7a7f87;
  --paper:#ffffff;
  --stage:#e8e9ec;
  --photo-a:#8f9aa8;
  --photo-b:#c9ced6;
}
*{margin:0;padding:0;box-sizing:border-box}
html,body{width:1051px;height:1200px;overflow:hidden;background:var(--stage)}
body{position:relative;font-family:'Open Sans',sans-serif;color:var(--ink)}
.slide{position:absolute;width:317px;height:178px;background:var(--paper);overflow:hidden;box-shadow:0 1px 3px rgba(0,0,0,.18);border-bottom:1.5px solid var(--blue)}
.c0{left:39px}.c1{left:367px}.c2{left:695px}
.r0{top:38px}.r1{top:227px}.r2{top:416px}.r3{top:605px}.r4{top:794px}.r5{top:981px}
.abs{position:absolute}
.logo{position:absolute;right:10px;top:7px;font:700 9px 'Montserrat',sans-serif;color:var(--blue);letter-spacing:-.2px}
.pg{position:absolute;left:6px;bottom:4px;font:400 4px 'Open Sans',sans-serif;color:var(--ink)}
.title{position:absolute;font:600 10.5px/1.15 'Montserrat',sans-serif;color:var(--blue)}
.title.rule::after{content:"";display:block;width:22px;height:1.8px;background:var(--orange);margin-top:5px}
.tiny{font:400 3.3px/1.4 'Open Sans',sans-serif;color:var(--grey)}
.tiny.w{color:#fff}
.label{font:700 5px 'Montserrat',sans-serif;color:var(--ink)}
.item-h{font:600 6px 'Montserrat',sans-serif;color:var(--blue)}
.item-h .n{color:var(--orange);margin-right:2px}
.photo{position:absolute;background:linear-gradient(135deg,var(--photo-a),var(--photo-b))}
.sq{position:absolute;background:var(--orange)}
.blue{background:var(--blue)}
.num-box{display:inline-block;flex:none;width:11px;height:11px;background:var(--blue);color:#fff;font:700 6px/11px 'Montserrat',sans-serif;text-align:center;margin-right:5px;vertical-align:top;outline:1.5px solid #fff;outline-offset:-2.5px}
.icon-sq{position:absolute;width:24px;height:24px;background:var(--orange);display:flex;align-items:center;justify-content:center}
.icon-sq.b{background:var(--blue)}
.center{text-align:center}
.contact-dot{display:inline-block;width:6px;height:6px;background:var(--orange);vertical-align:-1px;margin-right:3px}
</style>
</head>
<body>

<!-- 1 Cover -->
<section class="slide c0 r0">
  <div class="photo" role="img" aria-label="Cover photo toned in orange and blue" style="inset:0;background:linear-gradient(100deg,#b7622a 0%,#6b5a66 35%,#2c64a8 70%,#24569a 100%)"></div>
  <div class="abs" style="left:82px;top:62px;font:700 34px 'Montserrat',sans-serif;color:#fff;letter-spacing:-1px">Corvenna</div>
  <div class="abs" style="left:80px;top:112px;width:237px;height:11px;background:var(--orange);border-radius:5px 0 0 5px;font:600 7px/11px 'Montserrat',sans-serif;color:#fff;letter-spacing:3.2px;padding-left:16px">Business Marketing</div>
</section>

<!-- 2 Title -->
<section class="slide c1 r0">
  <div class="sq" style="left:25px;top:0;width:73px;height:5px"></div>
  <div class="sq" style="left:200px;top:0;width:117px;height:9px"></div>
  <div class="sq" style="left:305px;top:0;width:12px;height:92px"></div>
  <div class="abs blue" style="left:124px;top:157px;width:193px;height:21px"></div>
  <div class="photo" role="img" aria-label="Photo of two colleagues talking in an office" style="left:160px;top:18px;width:141px;height:145px"></div>
  <div class="abs blue" style="left:289px;top:22px;width:7px;height:7px"></div>
  <div class="abs" style="left:19px;top:27px;font:700 21px 'Montserrat',sans-serif;color:var(--blue);letter-spacing:-.6px">Corvenna</div>
  <div class="abs" style="left:19px;top:84px;width:1.5px;height:49px;background:var(--orange)"></div>
  <div class="abs" style="left:23px;top:84px;font:500 8px 'Montserrat',sans-serif;color:var(--blue)">Presentation</div>
  <div class="abs" style="left:23px;top:94px;font:800 18px 'Montserrat',sans-serif;color:var(--orange)">Business</div>
  <div class="abs" style="left:23px;top:114px;font:700 14.5px 'Montserrat',sans-serif;color:var(--blue)">Marketing</div>
  <div class="abs" style="left:25px;top:160px;font:500 5px 'Montserrat',sans-serif;color:var(--blue);letter-spacing:2px">www.<span style="color:var(--orange)">website</span>.com</div>
</section>

<!-- 3 Agenda list -->
<section class="slide c2 r0">
  <div class="title rule" style="left:10px;top:9px">Text Added Here</div>
  <div class="logo">Corvenna</div>
  <div class="photo" role="img" aria-label="Top-down photo of a team meeting around a table" style="left:34px;top:42px;width:103px;height:106px"></div>
  <div class="abs" style="left:155px;top:43px;width:130px">
    <div class="item-h"><span class="n">1.</span>Lorem ipsum</div>
    <div class="tiny" style="margin:2px 0 0 8px">Lorem ipsum dolor sit amet, consectetuer adipiscing elit, sed diam nonummy nibh euismod tincid</div>
    <div class="item-h" style="margin-top:13px"><span class="n">2.</span>Lorem ipsum</div>
    <div class="tiny" style="margin:2px 0 0 8px">Lorem ipsum dolor sit amet, consectetuer adipiscing elit, sed diam nonummy nibh euismod tincid</div>
    <div class="item-h" style="margin-top:13px"><span class="n">3.</span>Lorem ipsum</div>
    <div class="tiny" style="margin:2px 0 0 8px">Lorem ipsum dolor sit amet, consectetuer adipiscing elit, sed diam nonummy nibh euismod tincid</div>
    <div class="item-h" style="margin-top:12px"><span class="n">4.</span>Lorem ipsum</div>
    <div class="tiny" style="margin:2px 0 0 8px">Lorem ipsum dolor sit amet, consectetuer adipiscing elit, sed diam nonummy nibh euismod tincid</div>
  </div>
  <div class="pg">2</div>
</section>

<!-- 4 Our Company -->
<section class="slide c0 r1">
  <div class="abs blue" style="left:0;top:0;width:49px;height:13px"></div>
  <div class="abs blue" style="left:0;top:0;width:16px;height:108px"></div>
  <div class="title rule" style="left:27px;top:21px;font-size:12px">Our<br>Company</div>
  <div class="tiny abs" style="left:27px;top:62px;width:112px;text-align:justify">Lorem ipsum dolor sit amet, consectetuer adipiscing elit, sed diam nonummy nibh euismod tincidunt ut laoreet dolore magna aliquam erat volutpat. Ut wisi enim ad minim veniam, quis nostrud exerci tation ullamcorper suscipit lobortis nisl ut aliquip ex ea commodo consequat. Duis autem vel eum iriure dolor in hendrerit in.<br><br>Lorem ipsum dolor sit amet, consectetuer adipiscing elit, sed diam nonummy nibh euismod tincidunt ut laoreet dolore magna aliquam erat volutpat. Ut wisi enim ad minim veniam, quis nostrud exerci tation ullamcorper suscipit lobortis nisl ut aliquip ex ea commodo consequat. Duis autem vel eum iriure dolor in hendrerit in vulputate velit esse molestie consequat.</div>
  <div class="logo">Corvenna</div>
  <svg class="abs" style="left:0;top:0" width="317" height="178" viewBox="0 0 317 178">
    <g fill="none" stroke-width="1.2">
      <circle cx="192" cy="44" r="13" fill="#f07a22"/><circle cx="192" cy="44" r="10.5" stroke="#fff"/>
      <circle cx="267" cy="44" r="13" fill="#2c64a8"/><circle cx="267" cy="44" r="10.5" stroke="#fff"/>
      <circle cx="192" cy="108" r="13" fill="#2c64a8"/><circle cx="192" cy="108" r="10.5" stroke="#fff"/>
      <circle cx="267" cy="108" r="13" fill="#f07a22"/><circle cx="267" cy="108" r="10.5" stroke="#fff"/>
      <g stroke="#fff" stroke-width=".9">
        <rect x="187" y="39" width="10" height="7" rx="1"/><path d="M189 49h6"/>
        <circle cx="267" cy="44" r="5"/><path d="M262 44h10M267 39v10"/>
        <circle cx="192" cy="108" r="5"/><path d="M192 105v6M190.5 106.5h3"/>
        <path d="M263 112l3-5 3 2 3-5"/>
      </g>
    </g>
  </svg>
  <div class="abs center" style="left:160px;top:60px;width:64px"><div class="label">LOREM IPSUM</div><div class="tiny" style="margin-top:1px">Lorem ipsum dolor sit amet, consectetuer adipiscing elit, sed diam nonummy nibh euismod tincid</div></div>
  <div class="abs center" style="left:235px;top:60px;width:64px"><div class="label">LOREM IPSUM</div><div class="tiny" style="margin-top:1px">Lorem ipsum dolor sit amet, consectetuer adipiscing elit, sed diam nonummy nibh euismod tincid</div></div>
  <div class="abs center" style="left:160px;top:124px;width:64px"><div class="label">LOREM IPSUM</div><div class="tiny" style="margin-top:1px">Lorem ipsum dolor sit amet, consectetuer adipiscing elit, sed diam nonummy nibh euismod tincid</div></div>
  <div class="abs center" style="left:235px;top:124px;width:64px"><div class="label">LOREM IPSUM</div><div class="tiny" style="margin-top:1px">Lorem ipsum dolor sit amet, consectetuer adipiscing elit, sed diam nonummy nibh euismod tincid</div></div>
  <div class="pg">3</div>
</section>

<!-- 5 Process -->
<section class="slide c1 r1">
  <div class="title rule" style="left:10px;top:9px">Text Added Here</div>
  <div class="logo">Corvenna</div>
  <div class="abs" role="img" aria-label="Faint world map in the background" style="left:55px;top:42px;width:210px;height:90px;background:#f3f4f6;border-radius:20px"></div>
  <svg class="abs" style="left:0;top:0" width="317" height="178" viewBox="0 0 317 178">
    <g fill="#fff" stroke="#2c64a8" stroke-width="1.6">
      <path d="M62 46h44a5 5 0 0 1 5 5v15M111 78v43a5 5 0 0 1-5 5H62a5 5 0 0 1-5-5V51a5 5 0 0 1 5-5"/>
      <path d="M135 46h44a5 5 0 0 1 5 5v15M184 78v43a5 5 0 0 1-5 5H135a5 5 0 0 1-5-5V100M130 88V51a5 5 0 0 1 5-5"/>
      <path d="M208 46h44a5 5 0 0 1 5 5v70a5 5 0 0 1-5 5H208a5 5 0 0 1-5-5V100M203 88V51a5 5 0 0 1 5-5"/>
      <path d="M111 72 L130 94" fill="none"/><path d="M184 72 L203 94" fill="none"/>
    </g>
    <g fill="#2c64a8"><circle cx="111" cy="72" r="2.4"/><circle cx="130" cy="94" r="2.4"/><circle cx="184" cy="72" r="2.4"/><circle cx="203" cy="94" r="2.4"/></g>
    <g fill="none" stroke="#f07a22" stroke-width="1">
      <circle cx="84" cy="57" r="3"/><path d="M83 61h2"/>
      <rect x="152" y="56" width="9" height="6"/><path d="M152 56l4.5 3.5 4.5-3.5"/>
      <path d="M226 55v7h8M227 61l3-3 2 1 2-3"/>
    </g>
  </svg>
  <div class="abs center" style="left:60px;top:66px;width:48px"><div class="label" style="font-size:4.8px">IDEA</div><div class="tiny" style="font-size:2.9px;margin-top:2px">Lorem ipsum dolor sit amet, consectetuer adipiscing elit, sed diam nonummy nibh euismod tincidunt ut laoreet dolore magna aliquam erat volutpat. Ut wisi enim ad minim veniam, quis nostrud exerci tation</div></div>
  <div class="abs center" style="left:133px;top:66px;width:48px"><div class="label" style="font-size:4.8px">PROMOTION</div><div class="tiny" style="font-size:2.9px;margin-top:2px">Lorem ipsum dolor sit amet, consectetuer adipiscing elit, sed diam nonummy nibh euismod tincidunt ut laoreet dolore magna aliquam erat volutpat. Ut wisi enim ad minim veniam, quis nostrud exerci tation</div></div>
  <div class="abs center" style="left:206px;top:66px;width:48px"><div class="label" style="font-size:4.8px">GROWTH</div><div class="tiny" style="font-size:2.9px;margin-top:2px">Lorem ipsum dolor sit amet, consectetuer adipiscing elit, sed diam nonummy nibh euismod tincidunt ut laoreet dolore magna aliquam erat volutpat. Ut wisi enim ad minim veniam, quis nostrud exerci tation</div></div>
  <div class="tiny abs center" style="left:35px;top:137px;width:247px">Lorem ipsum dolor sit amet, consectetuer adipiscing elit, sed diam nonummy nibh euismod tincidunt ut laoreet dolore magna aliquam erat volutpat. Ut wisi enim ad minim veniam, quis nostrud exerci tation ullamcorper suscipit lobortis nisl ut aliquip ex ea commodo consequat. Duis autem vel eum iriure dolor in hendrerit.</div>
  <div class="pg">4</div>
</section>

<!-- 6 Split statement -->
<section class="slide c2 r1">
  <div class="sq" style="left:0;top:0;width:11px;height:11px"></div>
  <div class="logo">Corvenna</div>
  <div class="abs" style="left:22px;top:23px;font:600 13px/1.55 'Montserrat',sans-serif;color:var(--blue)">Lorem Ipsum<br>Dolor Sit<br>Ametkeeper.</div>
  <div class="abs blue" style="left:0;top:95px;width:127px;height:55px;padding:8px 12px 0 22px">
    <div class="tiny w" style="font-size:3.4px">Lorem ipsum dolor sit amet, consectetuer adipiscing elit, sed diam nonummy nibh euismod tincidunt erat volutpat.<br><br>Ut wisi enim ad minim veniam, quis nostrud exerci tation ullamcorper suscipit lobortis nisl ut aliquip ex ea commodo consequat.</div>
  </div>
  <div class="icon-sq" style="left:144px;top:31px"><svg width="14" height="12" viewBox="0 0 14 12" fill="#fff"><circle cx="7" cy="3" r="2.3"/><circle cx="2.5" cy="4.5" r="1.6"/><circle cx="11.5" cy="4.5" r="1.6"/><path d="M3 12a4 4 0 0 1 8 0zM0 11a2.5 2.5 0 0 1 4-2v2zM14 11a2.5 2.5 0 0 0-4-2v2z"/></svg></div>
  <div class="icon-sq" style="left:144px;top:74px"><svg width="12" height="14" viewBox="0 0 12 14" fill="#fff"><circle cx="3" cy="2" r="1.7"/><circle cx="9" cy="2" r="1.7"/><rect x="1" y="4.5" width="4" height="9" rx="1"/><rect x="7" y="4.5" width="4" height="9" rx="1"/></svg></div>
  <div class="icon-sq" style="left:144px;top:119px"><svg width="14" height="12" viewBox="0 0 14 12" fill="#fff"><path d="M7 7 3.5 3.7A2 2 0 0 1 7 1.5a2 2 0 0 1 3.5 2.2z"/><path d="M0 9h4l3 1.5 5-2.5 1 1-6 3H0z"/></svg></div>
  <div class="abs" style="left:179px;top:32px;width:128px"><div class="item-h" style="font-weight:700;font-size:6.8px">We Before Me</div><div class="tiny" style="margin-top:3px">ipsum dolor sit amet, cons ectetuer adipiscing elit, sed diam nonummy nibh euismod tincidunt ut laoreet</div></div>
  <div class="abs" style="left:179px;top:74px;width:128px"><div class="item-h" style="font-weight:700;font-size:6.8px">We Are Good People</div><div class="tiny" style="margin-top:3px">ipsum dolor sit amet, cons ectetuer adipiscing elit, sed diam nonummy nibh euismod tincidunt ut laoreet dolore magna aliquam erat volutpat.</div></div>
  <div class="abs" style="left:179px;top:120px;width:128px"><div class="item-h" style="font-weight:700;font-size:6.8px">We Work with Heart</div><div class="tiny" style="margin-top:3px">ipsum dolor sit amet, cons ectetuer adipiscing elit, sed diam nonummy nibh euismod tincidunt</div></div>
  <div class="pg">5</div>
</section>

<!-- 7 Charts -->
<section class="slide c0 r2">
  <div class="abs blue" style="left:0;top:0;width:154px;height:92px;padding:13px 14px 0 14px">
    <div style="font:600 10px 'Montserrat',sans-serif;color:#fff">Text Added Here</div>
    <div style="width:22px;height:1.6px;background:var(--orange);margin:4px 0 4px"></div>
    <div style="font:400 5px/1.25 'Open Sans',sans-serif;color:#fff">Lorem ipsum dolor sit amet, consectetuer adipiscing elit, sed diam nonummy nibh euismod tincidunt ut laoreet dolore magna aliquam erat volutpat. Ut wisi enim ad minim veniam<br><br>quis nostrud exerci tation ullamcorper suscipit lobortis nisl ut aliquip ex ea commodo conse-</div>
  </div>
  <div class="logo">Corvenna</div>
  <svg class="abs" style="left:0;top:0" width="317" height="178" viewBox="0 0 317 178" font-family="Open Sans" font-size="3.6" fill="#555">
    <g stroke="#ddd" stroke-width=".4">
      <path d="M170 31h120M170 41h120M170 51h120M170 61h120M170 71h120M170 81h120M170 91h120M290 31v60"/>
      <path d="M23 110h150M23 118h150M23 126h150M23 134h150M23 142h150M23 150h150M23 158h150M173 110v48"/>
    </g>
    <g text-anchor="end"><text x="167" y="32">60</text><text x="167" y="42">50</text><text x="167" y="52">40</text><text x="167" y="62">30</text><text x="167" y="72">20</text><text x="167" y="82">10</text><text x="167" y="92">0</text></g>
    <g fill="#2c64a8"><rect x="184" y="51" width="3.5" height="40"/><rect x="219" y="56" width="3.5" height="35"/><rect x="246" y="78" width="3.5" height="13"/><rect x="267" y="39" width="3.5" height="52"/></g>
    <g fill="#f07a22"><rect x="190" y="41" width="3.5" height="50"/><rect x="213" y="81" width="3.5" height="10"/><rect x="240" y="33" width="3.5" height="58"/><rect x="273" y="61" width="3.5" height="30"/></g>
    <g text-anchor="middle" font-size="4.2"><text x="189" y="99">JAN</text><text x="218" y="99">FEB</text><text x="245" y="99">MAR</text><text x="272" y="99">APR</text></g>
    <g text-anchor="end" font-size="3.4"><text x="21" y="111">60</text><text x="21" y="119">50</text><text x="21" y="127">40</text><text x="21" y="135">30</text><text x="21" y="143">20</text><text x="21" y="151">10</text><text x="21" y="159">0</text></g>
    <polyline fill="none" stroke="#2c64a8" stroke-width=".8" points="30,158 44,154 58,139 72,150 86,130 100,145 114,149 128,137 142,129 156,124"/>
    <polyline fill="none" stroke="#f07a22" stroke-width=".8" points="30,147 44,151 58,134 72,117 86,128 100,137 114,143 128,147 142,139 156,150"/>
    <g fill="#2c64a8"><circle cx="30" cy="158" r="1"/><circle cx="58" cy="139" r="1"/><circle cx="86" cy="130" r="1"/><circle cx="114" cy="149" r="1"/><circle cx="142" cy="129" r="1"/><circle cx="156" cy="124" r="1"/></g>
    <g fill="#f07a22"><circle cx="44" cy="151" r="1"/><circle cx="72" cy="117" r="1"/><circle cx="100" cy="137" r="1"/><circle cx="128" cy="147" r="1"/></g>
    <g font-size="2.4" text-anchor="middle"><text x="30" y="164">TEXT 01</text><text x="44" y="164">TEXT 02</text><text x="58" y="164">TEXT 03</text><text x="72" y="164">TEXT 04</text><text x="86" y="164">TEXT 05</text><text x="100" y="164">TEXT 06</text><text x="114" y="164">TEXT 07</text><text x="128" y="164">TEXT 08</text><text x="142" y="164">TEXT 09</text></g>
    <circle cx="164" cy="116" r="2.2" fill="#2c64a8"/><circle cx="241" cy="116" r="2.2" fill="#f07a22"/>
    <circle cx="164" cy="138" r="2.2" fill="#f07a22"/><circle cx="241" cy="138" r="2.2" fill="#2c64a8"/>
  </svg>
  <div class="abs" style="left:170px;top:113px;width:60px"><div class="label" style="font-weight:600;font-size:4.8px">Lorem ipsum</div><div class="tiny" style="font-size:2.8px">Lorem ipsum dolor sit amet, consectetuer adipiscing elit, sed diam nonummy nibh euismod tincidunt ut laoreet</div></div>
  <div class="abs" style="left:247px;top:113px;width:60px"><div class="label" style="font-weight:600;font-size:4.8px">Lorem ipsum</div><div class="tiny" style="font-size:2.8px">Lorem ipsum dolor sit amet, consectetuer adipiscing elit, sed diam nonummy nibh euismod tincidunt ut laoreet</div></div>
  <div class="abs" style="left:170px;top:135px;width:60px"><div class="label" style="font-weight:600;font-size:4.8px">Lorem ipsum</div><div class="tiny" style="font-size:2.8px">Lorem ipsum dolor sit amet, consectetuer adipiscing elit, sed diam nonummy nibh euismod tincidunt ut laoreet</div></div>
  <div class="abs" style="left:247px;top:135px;width:60px"><div class="label" style="font-weight:600;font-size:4.8px">Lorem ipsum</div><div class="tiny" style="font-size:2.8px">Lorem ipsum dolor sit amet, consectetuer adipiscing elit, sed diam nonummy nibh euismod tincidunt ut laoreet</div></div>
  <div class="pg">6</div>
</section>

<!-- 8 Market Opportunities -->
<section class="slide c1 r2">
  <div class="sq" style="left:0;top:0;width:11px;height:11px"></div>
  <div class="logo">Corvenna</div>
  <div class="title" style="left:17px;top:19px;font-size:10px">Market<br>Opportunities.</div>
  <div class="abs blue" style="left:0;top:53px;width:109px;height:89px;padding:7px 10px 0 14px">
    <div style="font:400 5px/1.15 'Open Sans',sans-serif;color:#fff">Lorem ipsum dolor sit amet, consectetuer adipiscing elit, sed diam nonummy nibh euismod tincidunt ut laoreet dolore magna aliquam erat volutpat. Ut wisi enim ad minim veniam, quis nostrud exerci tation ullamcorper suscipit lobortis nisl ut aliquip ex ea commodo consequat. Duis autem vel eum iriure dolor in hendrerit i</div>
  </div>
  <div class="abs" style="left:131px;top:22px;font:500 5.6px 'Montserrat',sans-serif;color:var(--ink)">CONSECTETUER ADIPISCING</div>
  <svg class="abs" style="left:0;top:0" width="317" height="178" viewBox="0 0 317 178" font-family="Open Sans" font-size="5" fill="#555">
    <g stroke="#ddd" stroke-width=".4"><path d="M137 38h157M137 50h157M137 62h157M137 74h157M137 86h157M137 98h157M137 110h157M294 38v72M137 38v72"/></g>
    <g text-anchor="end"><text x="134" y="40">60</text><text x="134" y="52">50</text><text x="134" y="64">40</text><text x="134" y="76">30</text><text x="134" y="88">20</text><text x="134" y="100">10</text><text x="134" y="112">0</text></g>
    <rect x="153" y="44" width="17" height="66" fill="#2c64a8"/>
    <rect x="186" y="72" width="17" height="38" fill="#f07a22"/>
    <rect x="220" y="54" width="17" height="56" fill="#2c64a8"/>
    <rect x="254" y="77" width="17" height="33" fill="#f07a22"/>
    <g text-anchor="middle" font-size="5.2"><text x="161" y="121">JAN</text><text x="195" y="121">FEB</text><text x="228" y="121">MAR</text><text x="262" y="121">APR</text></g>
    <circle cx="127" cy="136" r="2.8" fill="#f07a22"/><circle cx="218" cy="136" r="2.8" fill="#2c64a8"/>
  </svg>
  <div class="abs" style="left:135px;top:133px;width:72px"><div class="label" style="font-weight:500;font-size:5.4px">Lorem ipsum</div><div class="tiny" style="font-size:2.9px">Lorem ipsum dolor sit amet, consectetuer adipiscing elit, sed diam nonummy nibh euismod tincidunt ut laoreet</div></div>
  <div class="abs" style="left:226px;top:133px;width:72px"><div class="label" style="font-weight:500;font-size:5.4px">Lorem ipsum</div><div class="tiny" style="font-size:2.9px">Lorem ipsum dolor sit amet, consectetuer adipiscing elit, sed diam nonummy nibh euismod tincidunt ut laoreet</div></div>
  <div class="pg">7</div>
</section>

<!-- 9 Image split -->
<section class="slide c2 r2">
  <div class="sq" style="left:0;top:0;width:94px;height:11px"></div>
  <div class="logo">Corvenna</div>
  <div class="title" style="left:17px;top:19px;font-size:13.5px">Subject<br>Title</div>
  <div class="tiny abs" style="left:17px;top:67px;width:72px;font-size:3.7px">Lorem ipsum dolor sit amet, consectetuer adipiscing elit, sed diam nonummy nibh euismod tincidunt ut laoreet dolore magna aliquam erat volutpat. Ut wisi enim ad minim veniam, quis nostrud exerci tation ullamcorper suscipit lobortis nisl ut aliquip ex ea commodo consequat. Duis autem vel eum iriure.</div>
  <div class="photo" role="img" aria-label="Photo of colleagues working at a laptop" style="left:94px;top:0;width:59px;height:110px"></div>
  <div class="abs blue" style="left:133px;top:38px;width:184px;height:112px"></div>
  <div class="photo" role="img" aria-label="Photo of two colleagues talking by a window" style="left:165px;top:60px;width:63px;height:102px"></div>
  <div class="abs" style="left:234px;top:64px;font:600 8.5px/1.2 'Montserrat',sans-serif;color:var(--orange)">Lorem Ipsum<br>Dolor Sit<br>Ametkeeper.</div>
  <div class="tiny w abs" style="left:237px;top:104px;width:70px;font-size:3.6px">Lorem ipsum dolor sit amet, consectetuer adipiscing<br><br>elit, sed diam nonummy nibh euismod tincidunt ut</div>
  <div class="pg">8</div>
</section>

<!-- 10 Cycle diagram -->
<section class="slide c0 r3">
  <div class="sq" style="left:0;top:0;width:11px;height:11px"></div>
  <div class="logo">Corvenna</div>
  <div class="title" style="left:16px;top:20px;font-size:10.5px">Subtitle Text</div>
  <div class="tiny abs" style="left:16px;top:40px;width:86px;font-size:4px">Lorem ipsum dolor sit amet, consectetuer adipiscing elit, sed diam nonummy nibh .<br><br>Ut wisi enim ad minim veniam, quis nostrud exerci tation ullamcorper suscipit lobortis. Ut wisi enim ad minim veniam, quis nostrud exerci tation ullamcorper suscipit lobortis. Ut wisi enim ad minim veniam, quis</div>
  <div class="abs blue" style="left:0;top:101px;width:102px;height:48px;padding:5px 0 0 17px">
    <div style="font:600 4.6px 'Montserrat',sans-serif;color:#fff">Lorem ipsum</div>
    <div class="tiny w" style="font-size:2.6px;width:80px">Lorem ipsum dolor sit amet, consectetuer adipiscing elit, sed diam nonummy nibh euismod</div>
    <div style="font:600 4.6px 'Montserrat',sans-serif;color:#fff;margin-top:7px">Lorem ipsum</div>
    <div class="tiny w" style="font-size:2.6px;width:80px">Lorem ipsum dolor sit amet, consectetuer adipiscing elit, sed diam nonummy nibh euismod</div>
  </div>
  <svg class="abs" style="left:0;top:0" width="317" height="178" viewBox="0 0 317 178">
    <circle cx="6" cy="108" r="2" fill="#fff"/><circle cx="6" cy="130" r="2" fill="#fff"/>
    <g fill="none" stroke="#2c64a8" stroke-width="2.2">
      <path d="M148 87 A55 55 0 0 1 248 56"/>
      <path d="M246 66 A55 55 0 0 1 256 111"/>
      <path d="M252 124 A52 52 0 0 1 195 145"/>
      <path d="M186 141 A52 52 0 0 1 158 123"/>
    </g>
    <path d="M143 84l5 8 5-8" fill="none" stroke="#2c64a8" stroke-width="2.2"/>
    <circle cx="157" cy="120" r="4" fill="#fff" stroke="#2c64a8" stroke-width="2"/>
    <g>
      <circle cx="238" cy="59" r="15" fill="#f07a22"/><circle cx="238" cy="59" r="10" fill="#fff"/>
      <circle cx="238" cy="59" r="7.5" fill="none" stroke="#2c64a8" stroke-width="1"/>
      <circle cx="238" cy="58" r="2.5" fill="none" stroke="#2c64a8" stroke-width=".9"/><path d="M240 60l2 2" stroke="#2c64a8"/>
      <circle cx="250" cy="104" r="12" fill="#f07a22"/><circle cx="250" cy="104" r="8" fill="#fff"/>
      <circle cx="250" cy="104" r="6" fill="none" stroke="#2c64a8" stroke-width="1"/><circle cx="250" cy="104" r="2" fill="#2c64a8"/>
      <circle cx="225" cy="143" r="9" fill="#f07a22"/><circle cx="225" cy="143" r="6" fill="#fff"/><path d="M225 139v7M222 144a3 3 0 0 0 6 0" stroke="#2c64a8" fill="none" stroke-width=".9"/>
      <circle cx="178" cy="131" r="9" fill="#f07a22"/><circle cx="178" cy="131" r="6" fill="#fff"/><circle cx="178" cy="132" r="2.2" fill="#2c64a8"/>
    </g>
    <g fill="#2c64a8"><rect x="173" y="64" width="2" height="8"/><rect x="176" y="61" width="2" height="11"/><rect x="179" y="66" width="2" height="6"/></g>
    <path d="M171 72h12" stroke="#f07a22" stroke-width=".8"/>
    <g font-family="Montserrat" font-weight="700" font-size="3.6" fill="#f07a22">
      <text x="264" y="41">85%</text><text x="219" y="90">80%</text><text x="191" y="126">50%</text><text x="247" y="158">75%</text>
    </g>
    <g stroke="#f07a22" stroke-width=".6" fill="none"><path d="M248 47l14-7"/><path d="M230 88h8"/><path d="M184 125h6"/><path d="M234 150l12 6"/></g>
    <g font-family="Montserrat" font-weight="600" font-size="4.6" fill="#333a44">
      <text x="164" y="82">MAIN TITLE</text>
      <text x="270" y="47">Your Title</text><text x="278" y="93">Your Title</text><text x="120" y="121">Your Title</text><text x="264" y="133">Your Title</text>
    </g>
  </svg>
  <div class="tiny abs center" style="left:163px;top:83px;width:28px;font-size:2.4px">Lorem ipsum dolor sit amet, consectetuer adipiscing elit, sed diam nonummy nibh euismod</div>
  <div class="tiny abs" style="left:263px;top:48px;width:37px;font-size:2.3px;text-align:right">Lorem ipsum dolor sit amet, consectetuer adipiscing elit, sed diam nonummy nibh euismod</div>
  <div class="tiny abs" style="left:263px;top:94px;width:37px;font-size:2.3px;text-align:right">Lorem ipsum dolor sit amet, consectetuer adipiscing elit, sed diam nonummy nibh euismod</div>
  <div class="tiny abs" style="left:112px;top:122px;width:34px;font-size:2.3px;text-align:right">Lorem ipsum dolor sit amet, consectetuer adipiscing elit, sed diam nonummy nibh euismod</div>
  <div class="tiny abs" style="left:262px;top:134px;width:34px;font-size:2.3px;text-align:right">Lorem ipsum dolor sit amet, consectetuer adipiscing elit, sed diam nonummy nibh euismod</div>
  <div class="pg">9</div>
</section>

<!-- 11 Section divider -->
<section class="slide c1 r3" style="border-bottom:0">
  <div class="photo" role="img" aria-label="City skyline photo tinted in deep blue" style="inset:0;background:linear-gradient(160deg,#3b6aa6 0%,#2c5f9f 45%,#2a5a98 100%)"></div>
  <div class="sq" style="left:7px;top:7px;width:8px;height:8px"></div>
  <div class="abs" style="left:20px;top:111px;width:1.2px;height:41px;background:var(--orange)"></div>
  <div class="abs" style="left:26px;top:110px;font:400 17px/1.12 'Montserrat',sans-serif;color:#fff">About<br><span style="font-weight:600">Our </span><span style="font-weight:700;color:var(--orange)">Company</span></div>
</section>

<!-- 12 Two columns -->
<section class="slide c2 r3">
  <div class="title rule" style="left:10px;top:9px">Text Added Here</div>
  <div class="logo">Corvenna</div>
  <div class="abs" style="left:31px;top:41px;width:119px">
    <div class="item-h" style="font-size:6px">1. Text Added Here</div>
    <div class="tiny" style="margin-top:1px;font-size:3.1px;text-align:justify">Lorem ipsum dolor sit amet, cons ectetuer adipiscing elit, sed diam nonummy nibh euismod tincidunt ut laoreet dolore magna aliquam erat volutpat. Ut wisi enim ad minim veniam, quis nostrud exerci tation ullamcorper suscipit lobortis nisl ut aliquip ex ea commodo consequat.<br><br>Lorem ipsum dolor sit amet, consectetuer adipiscing elit, sed diam nonummy nibh euismod tincidunt ut laoreet dolore magna aliquam erat volutpat. Ut wisi enim ad minim veniam, quis nostrud exerci tation ullamcorper suscipit lobortis nisl ut aliquip ex ea commodo consequat.</div>
  </div>
  <div class="abs" style="left:167px;top:41px;width:119px">
    <div class="item-h" style="font-size:6px">2. Text Added Here</div>
    <div class="tiny" style="margin-top:1px;font-size:3.1px;text-align:justify">Lorem ipsum dolor sit amet, cons ectetuer adipiscing elit, sed diam nonummy nibh euismod tincidunt ut laoreet dolore magna aliquam erat volutpat. Ut wisi enim ad minim veniam, quis nostrud exerci tation ullamcorper suscipit lobortis nisl ut aliquip ex ea commodo consequat.<br><br>Lorem ipsum dolor sit amet, consectetuer adipiscing elit, sed diam nonummy nibh euismod tincidunt ut laoreet dolore magna aliquam erat volutpat. Ut wisi enim ad minim veniam, quis nostrud exerci tation ullamcorper suscipit lobortis nisl ut aliquip ex ea commodo consequat.</div>
  </div>
  <div class="abs" style="left:38px;top:113px;width:110px;display:flex"><span class="num-box">1.</span><div><div class="label" style="font-weight:500;font-size:5.4px">Lorem ipsum</div><div class="tiny" style="font-size:2.8px">Lorem ipsum dolor sit amet, consectetuer adipiscing elit, sed diam nonummy nibh</div></div></div>
  <div class="abs" style="left:38px;top:141px;width:110px;display:flex"><span class="num-box" style="background:var(--orange)">2.</span><div><div class="label" style="font-weight:500;font-size:5.4px">Lorem ipsum</div><div class="tiny" style="font-size:2.8px">Lorem ipsum dolor sit amet, consectetuer adipiscing elit, sed diam nonummy nibh</div></div></div>
  <div class="abs" style="left:177px;top:112px;width:110px;display:flex"><span class="num-box" style="background:var(--orange)">1.</span><div><div class="label" style="font-weight:500;font-size:5.4px">Lorem ipsum</div><div class="tiny" style="font-size:2.8px">Lorem ipsum dolor sit amet, consectetuer adipiscing elit, sed diam nonummy nibh</div></div></div>
  <div class="abs" style="left:177px;top:140px;width:110px;display:flex"><span class="num-box">2.</span><div><div class="label" style="font-weight:500;font-size:5.4px">Lorem ipsum</div><div class="tiny" style="font-size:2.8px">Lorem ipsum dolor sit amet, consectetuer adipiscing elit, sed diam nonummy nibh</div></div></div>
  <div class="pg">11</div>
</section>

<!-- 13 Timemap -->
<section class="slide c0 r4">
  <div class="title rule" style="left:12px;top:9px">Our Timemap</div>
  <div class="logo">Corvenna</div>
  <svg class="abs" style="left:0;top:0" width="317" height="178" viewBox="0 0 317 178" font-family="Montserrat">
    <path d="M63 37v109h212" stroke="#999" stroke-width=".6" fill="none"/>
    <circle cx="63" cy="37" r="1.3" fill="#999"/>
    <g fill="#999"><circle cx="63" cy="146" r="1.3"/><circle cx="84" cy="146" r="1.3"/><circle cx="106" cy="146" r="1.3"/><circle cx="127" cy="146" r="1.3"/><circle cx="148" cy="146" r="1.3"/><circle cx="169" cy="146" r="1.3"/><circle cx="190" cy="146" r="1.3"/><circle cx="211" cy="146" r="1.3"/><circle cx="232" cy="146" r="1.3"/><circle cx="254" cy="146" r="1.3"/><circle cx="275" cy="146" r="1.3"/></g>
    <g font-size="5.4" fill="#fff" font-weight="500" text-anchor="middle">
      <rect x="63" y="46" width="31" height="17" fill="#f07a22"/><text x="78" y="56.5">20%</text>
      <rect x="94" y="46" width="43" height="17" fill="#2c64a8"/><text x="115" y="56.5">40%</text>
      <rect x="137" y="46" width="31" height="17" fill="#f07a22"/><text x="152" y="56.5">10%</text>
      <rect x="168" y="46" width="107" height="17" fill="#2c64a8"/><text x="221" y="56.5">90%</text>
      <rect x="63" y="70" width="74" height="17" fill="#2c64a8"/><text x="100" y="80.5">50%</text>
      <rect x="137" y="70" width="53" height="17" fill="#f07a22"/><text x="163" y="80.5">30%</text>
      <rect x="190" y="70" width="43" height="17" fill="#2c64a8"/><text x="212" y="80.5">20%</text>
      <rect x="233" y="70" width="42" height="17" fill="#f07a22"/><text x="254" y="80.5">20%</text>
      <rect x="63" y="95" width="43" height="17" fill="#2c64a8"/><text x="84" y="105.5">30%</text>
      <rect x="106" y="95" width="63" height="17" fill="#f07a22"/><text x="137" y="105.5">60%</text>
      <rect x="169" y="95" width="22" height="17" fill="#2c64a8"/><text x="180" y="105.5">10%</text>
      <rect x="191" y="95" width="84" height="17" fill="#f07a22"/><text x="233" y="105.5">70%</text>
    </g>
    <g font-size="6" fill="#2c64a8" font-weight="600"><text x="43" y="57">2019</text><text x="43" y="81">2020</text><text x="43" y="106">2021</text></g>
    <g fill="#f07a22">
      <circle cx="35" cy="55" r="2.4"/>
      <path d="M35 50v1.5M30.5 55h1.5M38 55h1.5M31.8 51.8l1 1M38.2 51.8l-1 1" stroke="#f07a22" stroke-width=".7"/>
      <path d="M35 74v8M32 79.5a3 3 0 0 0 6 0M33 75.5h4" stroke="#f07a22" stroke-width=".9" fill="none"/>
      <path d="M32 104a3 3.5 0 0 0 6 0c0-2-1.5-3-2-4h-2c-.5 1-2 2-2 4z"/><rect x="33.5" y="98" width="3" height="1.5"/>
    </g>
    <g font-size="5" fill="#333a44" text-anchor="middle"><text x="63" y="156">0%</text><text x="84" y="156">10%</text><text x="106" y="156">20%</text><text x="127" y="156">30%</text><text x="148" y="156">40%</text><text x="169" y="156">50%</text><text x="190" y="156">60%</text><text x="211" y="156">70%</text><text x="232" y="156">80%</text><text x="254" y="156">90%</text><text x="275" y="156">100%</text></g>
  </svg>
  <div class="abs" style="left:59px;top:160px;width:48px"><div class="item-h" style="font-weight:500;font-size:4.8px">Lorem Ipsum</div><div class="tiny" style="font-size:2.8px">Lorem ipsum dolor sit amet, consectetuer adipiscing elit, sed diam nonummy nibh euismod tincid</div></div>
  <div class="abs" style="left:117px;top:160px;width:48px"><div class="item-h" style="font-weight:500;font-size:4.8px;color:var(--orange)">Lorem Ipsum</div><div class="tiny" style="font-size:2.8px">Lorem ipsum dolor sit amet, consectetuer adipiscing elit, sed diam nonummy nibh euismod tincid</div></div>
  <div class="abs" style="left:177px;top:160px;width:48px"><div class="item-h" style="font-weight:500;font-size:4.8px">Lorem Ipsum</div><div class="tiny" style="font-size:2.8px">Lorem ipsum dolor sit amet, consectetuer adipiscing elit, sed diam nonummy nibh euismod tincid</div></div>
  <div class="abs" style="left:238px;top:160px;width:48px"><div class="item-h" style="font-weight:500;font-size:4.8px;color:var(--orange)">Lorem Ipsum</div><div class="tiny" style="font-size:2.8px">Lorem ipsum dolor sit amet, consectetuer adipiscing elit, sed diam nonummy nibh euismod tincid</div></div>
  <div class="pg">12</div>
</section>

<!-- 14 Icon grid -->
<section class="slide c1 r4">
  <div class="title rule" style="left:12px;top:11px">Text Added Here</div>
  <div class="logo">Corvenna</div>
  <div class="icon-sq b" style="left:58px;top:38px;outline:1px solid #fff;outline-offset:-3px"><svg width="14" height="10" viewBox="0 0 14 10" fill="none" stroke="#fff" stroke-width=".9"><circle cx="4" cy="3" r="2"/><circle cx="10" cy="3" r="2"/><path d="M0.5 9.5a3.5 3 0 0 1 7 0M6.5 9.5a3.5 3 0 0 1 7 0"/></svg></div>
  <div class="icon-sq" style="left:148px;top:38px;outline:1px solid #fff;outline-offset:-3px"><svg width="12" height="12" viewBox="0 0 12 12" fill="none" stroke="#fff" stroke-width=".9"><circle cx="4" cy="4" r="3"/><circle cx="8" cy="8" r="3"/></svg></div>
  <div class="icon-sq b" style="left:239px;top:38px;outline:1px solid #fff;outline-offset:-3px"><svg width="12" height="12" viewBox="0 0 12 12" fill="none" stroke="#fff" stroke-width=".9"><path d="M1 11h10M2 11V7h2v4M5 11V5h2v6M8 11V3h2v8M2 4l7-3"/></svg></div>
  <div class="icon-sq" style="left:58px;top:102px;outline:1px solid #fff;outline-offset:-3px"><svg width="12" height="12" viewBox="0 0 12 12" fill="none" stroke="#fff" stroke-width=".9"><path d="M1 1v10h10M3 3c1 5 4 6 7 6"/></svg></div>
  <div class="icon-sq b" style="left:148px;top:102px;outline:1px solid #fff;outline-offset:-3px"><svg width="10" height="13" viewBox="0 0 10 13" fill="none" stroke="#fff" stroke-width=".9"><path d="M3 1h4l-1 2.5h-2zM1 11c0-4 2-7 4-7s4 3 4 7zM5 6v4"/></svg></div>
  <div class="icon-sq" style="left:239px;top:102px;outline:1px solid #fff;outline-offset:-3px"><svg width="12" height="13" viewBox="0 0 12 13" fill="none" stroke="#fff" stroke-width=".9"><circle cx="6" cy="5" r="4"/><path d="M3.5 8.5 2 12l2-1 1 1.5M8.5 8.5 10 12l-2-1-1 1.5"/></svg></div>
  <div class="abs center" style="left:40px;top:66px;width:60px"><div class="label" style="font-weight:600;font-size:5px">Lorem ipsum</div><div class="tiny" style="font-size:2.8px">Lorem ipsum dolor sit amet, consectetuer adipiscing elit, sed diam nonummy nibh euismod tincidunt ut laoreet</div></div>
  <div class="abs center" style="left:130px;top:66px;width:60px"><div class="label" style="font-weight:600;font-size:5px">Lorem ipsum</div><div class="tiny" style="font-size:2.8px">Lorem ipsum dolor sit amet, consectetuer adipiscing elit, sed diam nonummy nibh euismod tincidunt ut laoreet</div></div>
  <div class="abs center" style="left:221px;top:66px;width:60px"><div class="label" style="font-weight:600;font-size:5px">Lorem ipsum</div><div class="tiny" style="font-size:2.8px">Lorem ipsum dolor sit amet, consectetuer adipiscing elit, sed diam nonummy nibh euismod tincidunt ut laoreet</div></div>
  <div class="abs center" style="left:40px;top:130px;width:60px"><div class="label" style="font-weight:600;font-size:5px">Lorem ipsum</div><div class="tiny" style="font-size:2.8px">Lorem ipsum dolor sit amet, consectetuer adipiscing elit, sed diam nonummy nibh euismod tincidunt ut laoreet</div></div>
  <div class="abs center" style="left:130px;top:130px;width:60px"><div class="label" style="font-weight:600;font-size:5px">Lorem ipsum</div><div class="tiny" style="font-size:2.8px">Lorem ipsum dolor sit amet, consectetuer adipiscing elit, sed diam nonummy nibh euismod tincidunt ut laoreet</div></div>
  <div class="abs center" style="left:221px;top:130px;width:60px"><div class="label" style="font-weight:600;font-size:5px">Lorem ipsum</div><div class="tiny" style="font-size:2.8px">Lorem ipsum dolor sit amet, consectetuer adipiscing elit, sed diam nonummy nibh euismod tincidunt ut laoreet</div></div>
  <div class="pg">13</div>
</section>

<!-- 15 Image with text -->
<section class="slide c2 r4">
  <div class="sq" style="left:9px;top:9px;width:8px;height:8px"></div>
  <div class="logo">Corvenna</div>
  <div class="title" style="left:23px;top:30px;font-size:10px;line-height:1.45">Creative Text<br>Heading Added<br>Here</div>
  <div class="photo" role="img" aria-label="Photo of a business team gathered around a laptop" style="left:123px;top:31px;width:192px;height:74px"></div>
  <div class="tiny abs" style="left:123px;top:108px;width:186px;font-size:3.5px">Lorem ipsum dolor sit amet, consectetuer adipiscing elit, sed diam nonummy nibh euismod tincidunt erat volutpat.<br><br>Ut wisi enim ad minim veniam, quis nostrud exerci tation ullamcorper suscipit lobortis nisl ut aliquip ex ea commodo consequat. Ut wisi enim ad minim veniam, quis nostrud exerci tation ullamcorper suscipit lobortis nisl ut aliquip ex ea commodo consequat.</div>
  <div class="abs" style="left:25px;top:90px;width:95px;display:flex"><span class="num-box">1.</span><div><div class="item-h" style="color:var(--orange);font-weight:500;font-size:4.6px">Lorem ipsum</div><div class="tiny" style="font-size:2.6px">Lorem ipsum dolor sit amet, consectetuer adipiscing elit, sed diam nonummy nibh</div></div></div>
  <div class="abs" style="left:25px;top:112px;width:95px;display:flex"><span class="num-box">2.</span><div><div class="item-h" style="color:var(--orange);font-weight:500;font-size:4.6px">Lorem ipsum</div><div class="tiny" style="font-size:2.6px">Lorem ipsum dolor sit amet, consectetuer adipiscing elit, sed diam nonummy nibh</div></div></div>
  <div class="abs" style="left:25px;top:134px;width:95px;display:flex"><span class="num-box">3.</span><div><div class="item-h" style="color:var(--orange);font-weight:500;font-size:4.6px">Lorem ipsum</div><div class="tiny" style="font-size:2.6px">Lorem ipsum dolor sit amet, consectetuer adipiscing elit, sed diam nonummy nibh</div></div></div>
  <div class="pg">14</div>
</section>

<!-- 16 Numbered list -->
<section class="slide c0 r5">
  <div class="title rule" style="left:17px;top:9px">Text Added Here</div>
  <div class="logo">Corvenna</div>
  <div class="abs" style="left:31px;top:44px;width:130px">
    <div style="display:flex;gap:3px"><span style="font:700 8.5px 'Montserrat',sans-serif;color:var(--orange)">01.</span><div><div class="item-h" style="font-size:4.8px">Aliquam Erat Volutpat</div><div class="tiny" style="font-size:2.9px">Lorem ipsum dolor sit amet, consectetuer adipiscing elit, sed diam nonummy nibh euismod</div></div></div>
    <div style="display:flex;gap:3px;margin-top:12px"><span style="font:700 8.5px 'Montserrat',sans-serif;color:var(--orange)">02.</span><div><div class="item-h" style="font-size:4.8px">Consectetuer Adipiscing Elit</div><div class="tiny" style="font-size:2.9px">Lorem ipsum dolor sit amet, consectetuer adipiscing elit, sed diam nonummy nibh euismod tincidunt ut laoreet</div></div></div>
    <div style="display:flex;gap:3px;margin-top:12px"><span style="font:700 8.5px 'Montserrat',sans-serif;color:var(--orange)">03.</span><div><div class="item-h" style="font-size:4.8px">Duis Autem Vel Eum</div><div class="tiny" style="font-size:2.9px">Lorem ipsum dolor sit amet, consectetuer adipiscing elit, sed diam nonummy nibh euismod tincidunt.</div></div></div>
    <div style="display:flex;gap:3px;margin-top:12px"><span style="font:700 8.5px 'Montserrat',sans-serif;color:var(--orange)">04.</span><div><div class="item-h" style="font-size:4.8px">Aliquam Erat Volutpat</div><div class="tiny" style="font-size:2.9px">Lorem ipsum dolor sit amet, consectetuer adipiscing elit, sed diam nonummy nibh euismod tincidunt ut laoreet.</div></div></div>
  </div>
  <div class="abs blue" style="left:176px;top:44px;width:101px;height:106px"></div>
  <svg class="abs" style="left:0;top:0" width="317" height="178" viewBox="0 0 317 178">
    <g fill="#f07a22" stroke="#fff" stroke-width="1.4">
      <circle cx="176" cy="68" r="11"/><circle cx="176" cy="98" r="11"/><circle cx="176" cy="130" r="11"/>
    </g>
    <g fill="none" stroke="#fff" stroke-width=".9">
      <rect x="171" y="64" width="10" height="7"/><path d="M176 71v3M173 74h6"/>
      <path d="M171 98a3 3 0 0 1 2-4 4 4 0 0 1 7 1 2.5 2.5 0 0 1 0 5h-9zM176 100v4"/>
      <circle cx="172" cy="131" r="1.5"/><circle cx="180" cy="127" r="1.5"/><circle cx="180" cy="134" r="1.5"/><path d="M173.5 130.5l5-3M173.5 131.5l5 2"/>
    </g>
  </svg>
  <div class="abs" style="left:195px;top:58px;width:78px"><div style="font:600 7px 'Montserrat',sans-serif;color:#fff">Lorem ipsum</div><div class="tiny w" style="font-size:3.1px;margin-top:1px">Lorem ipsum dolor sit amet, cons ectetuer adipiscing elit, sed diam nonummy nibh euismod tincidunt ut laoreet</div></div>
  <div class="abs" style="left:195px;top:89px;width:78px"><div style="font:600 7px 'Montserrat',sans-serif;color:#fff">Lorem ipsum</div><div class="tiny w" style="font-size:3.1px;margin-top:1px">Lorem ipsum dolor sit amet, cons ectetuer adipiscing elit, sed diam nonummy nibh euismod tincidunt ut laoreet</div></div>
  <div class="abs" style="left:195px;top:121px;width:78px"><div style="font:600 7px 'Montserrat',sans-serif;color:#fff">Lorem ipsum</div><div class="tiny w" style="font-size:3.1px;margin-top:1px">Lorem ipsum dolor sit amet, cons ectetuer adipiscing elit, sed diam nonummy nibh euismod tincidunt</div></div>
  <div class="pg">15</div>
</section>

<!-- 17 Team -->
<section class="slide c1 r5">
  <div class="title rule" style="left:15px;top:13px">Our Team Members</div>
  <div class="logo">Corvenna</div>
  <div class="tiny abs" style="left:15px;top:38px;width:293px;font-size:3.5px;text-align:justify">Lorem ipsum dolor sit amet, consectetuer adipiscing elit, sed diam nonummy nibh euismod tincidunt ut laoreet dolore magna aliquam erat volutpat. Ut wisi enim ad minim veniam, quis nostrud exerci tation ullamcorper suscipit lobortis nisl ut aliquip ex ea commodo consequat. Duis autem vel eum iriure dolor in hendrerit in vulputate velit esse molestie consequat, vel illum dolore eu feugiat nulla facilisis at vero eros et accumsan et iusto odio dignissim qui blandit praesent luptatum zzril delenit augue duis dolore te feugait nulla facilisi.<br><br>Lorem ipsum dolor sit amet, cons ectetuer adipiscing elit, sed diam nonummy nibh euismod tincidunt ut laoreet dolore magna aliquam erat volutpat. Ut wisi enim ad minim veniam, quis nostrud exerci tation ullamcorper suscipit lobortis nisl ut aliquip ex ea</div>
  <div class="abs blue" style="left:0;top:93px;width:317px;height:57px"></div>
  <div class="abs" role="img" aria-label="Team member portrait placeholder" style="left:30px;top:80px;width:26px;height:26px;border-radius:50%;background:#e4e6ea;border:1.5px solid #fff"></div>
  <div class="abs" role="img" aria-label="Team member portrait placeholder" style="left:106px;top:80px;width:26px;height:26px;border-radius:50%;background:#e4e6ea;border:1.5px solid #fff"></div>
  <div class="abs" role="img" aria-label="Team member portrait placeholder" style="left:180px;top:80px;width:26px;height:26px;border-radius:50%;background:#e4e6ea;border:1.5px solid #fff"></div>
  <div class="abs" role="img" aria-label="Team member portrait placeholder" style="left:256px;top:80px;width:26px;height:26px;border-radius:50%;background:#e4e6ea;border:1.5px solid #fff"></div>
  <div class="abs center" style="left:13px;top:110px;width:60px"><div style="font:700 5.4px 'Montserrat',sans-serif;color:var(--orange)">JOHN SMITH</div><div class="tiny w" style="font-size:2.5px">ipsum dolor sit amet, cons ectetuer adipiscing elit, sed diam nonummy nibh euismod tincidunt ut laoreet dolore magna aliquam erat volutpat. Ut wisi enim ad minim veniam, quis nostrud</div></div>
  <div class="abs center" style="left:89px;top:110px;width:60px"><div style="font:700 5.4px 'Montserrat',sans-serif;color:var(--orange)">MILLIE SMITH</div><div class="tiny w" style="font-size:2.5px">ipsum dolor sit amet, cons ectetuer adipiscing elit, sed diam nonummy nibh euismod tincidunt ut laoreet dolore magna aliquam erat volutpat. Ut wisi enim ad minim veniam, quis nostrud</div></div>
  <div class="abs center" style="left:163px;top:110px;width:60px"><div style="font:700 5.4px 'Montserrat',sans-serif;color:var(--orange)">JOHN SMITH</div><div class="tiny w" style="font-size:2.5px">ipsum dolor sit amet, cons ectetuer adipiscing elit, sed diam nonummy nibh euismod tincidunt ut laoreet dolore magna aliquam erat volutpat. Ut wisi enim ad minim veniam, quis nostrud</div></div>
  <div class="abs center" style="left:239px;top:110px;width:60px"><div style="font:700 5.4px 'Montserrat',sans-serif;color:var(--orange)">MILLIE SMITH</div><div class="tiny w" style="font-size:2.5px">ipsum dolor sit amet, cons ectetuer adipiscing elit, sed diam nonummy nibh euismod tincidunt ut laoreet dolore magna aliquam erat volutpat. Ut wisi enim ad minim veniam, quis nostrud</div></div>
  <div class="pg">16</div>
</section>

<!-- 18 Closing -->
<section class="slide c2 r5" style="border-bottom:0">
  <div class="abs blue" style="left:205px;top:0;width:112px;height:178px"></div>
  <div class="abs" style="left:0;top:149px;width:205px;height:15px;background:#eef0f3"></div>
  <div class="abs" style="left:28px;top:56px;font:700 23px 'Montserrat',sans-serif;color:var(--blue);letter-spacing:-.6px">Corvenna</div>
  <div class="abs" style="left:28px;top:90px;font:400 5.4px/2.2 'Open Sans',sans-serif;color:var(--ink)">
    <div><span class="contact-dot"></span>+00 555 210 94</div>
    <div><span class="contact-dot"></span>hello@corvennapartners.com</div>
    <div><span class="contact-dot"></span>www.corvennapartners.com</div>
  </div>
  <div class="abs" style="left:28px;top:152px;font:600 6px 'Montserrat',sans-serif;color:var(--blue);letter-spacing:2.4px">www.<span style="color:var(--orange)">website</span>.com</div>
</section>

</body>
</html>
```